Organic Sunscreen Business "VelloBloom" Needs Package Design

Our company VelloBloom, manufactures an anti-ageing SPF 15 sunscreen product.

We specialise in the world's most rare and luxury organic anti-ageing ingredients.

We require an attractive package design for a 2.5 oz/75 ml squeezy bottle with box design, a few examples of similar examples which we like are attached.

We have a logo, barcode and graphic, which has been uploaded, and the bottle is to convey the message of wealth and luxury as well as organic sunscreen, we would prefer the package to be colourful and creative in order to sell.

I have included 2 rough sketches of the basic elements and layout of the design. And the box is to be similar to the bottle but to contain an extra caption.

Also, the sketch is only for a guide on how I would like the package, i.e. the labels and graphics can be in different positions/layouts thanks. And any additional creative images, text or fonts would be considered.
Updates

Industry/Entity Type

Business

Requirements
Must have
• FRONT of Bottle:
• LABEL 1: Logo (attached)
• LABEL 2:
• SPF 15
• Non-Nano
• Technology
• 100% Organic
• Paraben Free
• LABEL 3: (Larger/higher emphasis than Label 2)
• Anti-Ageing
• Moisturiser
• BACK of Bottle:
• Introduction: (For me to add personally at later date)
• Warnings: For external use only. Do not use on damaged or broken skin. Stop use and ask a doctor if rash occurs. When using this product keep out of eyes. Rinse with water to remove.
• Directions: Shake well before use. Apply liberally 15 minutes before sun exposure. Use a water resistant sunscreen if swimming or sweating. Reapply at least every 2 hours. Children under 6 months: Ask a doctor.
• Active Ingredient: Non-Nano Zinc Oxide (6%)
• Also contains: (For me to add personally at later date)
• Barcode: (image attached)
• Contact: www.vellobloom-example.com.au
• 2.5oz/7ml e
• BOX:
• Same as bottle, but one side will contain the caption:
• "7 NATURAL WONDERS IN 1" (In a creative style)
Nice to have
• Additional Text/Images/Fonts relating to the subject(s)
• Most creative design will be the winner.

```html
<!DOCTYPE html>
<html lang="en">
<head>
<meta charset="utf-8">
<title>VelloBloom Anti-Ageing Moisturiser – Packaging</title>
<link href="https://fonts.googleapis.com/css2?family=Cinzel:wght@500&family=Roboto+Condensed:wght@400;500&family=Tinos:wght@700&display=swap" rel="stylesheet">
<style>
  :root {
    --bg: #ffffff;
    --panel-top: #eaf6f9;
    --panel-bottom: #f6fbfc;
    --pink: #e0245e;
    --deep-red: #c8173f;
    --ink: #222222;
    --muted: #8a9aa0;
    --gold: #c99a3c;
    --gold-light: #e9cf8a;
    --green: #9bc43a;
    --red-band: #e0394a;
    --petal: #d9317a;
    --leaf: #4e8a3a;
    --skin: #e6c1a6;
    --hair: #6b4a3a;
    --silver: #c9cdd1;
    --silver-dark: #8e959b;
  }
  * { box-sizing: border-box; margin: 0; padding: 0; }
  html, body { width: 1200px; height: 1133px; overflow: hidden; background: var(--bg); }
  body { position: relative; font-family: "Roboto Condensed", sans-serif; color: var(--ink); }

  .panel {
    position: absolute;
    background: linear-gradient(180deg, var(--panel-top), var(--panel-bottom));
    text-align: center;
    overflow: hidden;
  }
  .box-side  { left: 150px; top: 120px; width: 260px; height: 880px; border-right: 1px solid #d4e4e8; }
  .box-front { left: 410px; top: 120px; width: 260px; height: 880px; }
  .tube      { left: 760px; top: 80px;  width: 280px; height: 860px; background: linear-gradient(90deg, #f1f3f4, #ffffff 40%, #f3f6f7); border-radius: 4px 4px 0 0; }

  .brand-mark {
    display: flex; flex-direction: column; align-items: center; gap: 10px;
    margin-top: 60px;
  }
  .brand-mark .dot { width: 18px; height: 18px; border-radius: 50%; background: var(--gold); }
  .brand-name { font-family: "Cinzel", serif; font-weight: 500; font-size: 22px; color: var(--ink); letter-spacing: 0.5px; }

  .product-title {
    margin: 40px auto 0; width: 200px;
    color: var(--pink); font-size: 24px; font-weight: 500; line-height: 1.2;
    padding-bottom: 8px; border-bottom: 1px solid var(--pink);
  }
  .flower {
    display: block; margin: 40px auto 0; width: 70px; height: 190px;
    background: linear-gradient(180deg, var(--petal) 0 30%, var(--leaf) 30% 100%);
    border-radius: 40px 40px 10px 10px;
  }
  .portrait {
    position: absolute; width: 150px; height: 200px;
    background: linear-gradient(180deg, var(--hair) 0 25%, var(--skin) 25% 100%);
    border-radius: 70px 70px 0 0;
  }
  .box-front .portrait { top: 470px; right: 20px; }
  .tube .portrait { top: 500px; left: 65px; }

  .claims { position: absolute; display: flex; font-size: 13px; font-weight: 500; color: #fff; white-space: nowrap; }
  .claims .organic { background: var(--green); padding: 4px 10px; }
  .claims .paraben { background: var(--red-band); padding: 4px 10px; }
  .box-front .claims { top: 660px; left: 22px; transform: rotate(-14deg); }
  .tube .claims { top: 695px; left: 50px; }

  .spf-seal {
    position: absolute; width: 66px; height: 66px; border-radius: 50%;
    background: var(--red-band); border: 3px solid var(--gold-light);
    color: #fff; font-size: 9px; line-height: 1.1;
    display: flex; flex-direction: column; justify-content: center; align-items: center;
  }
  .spf-seal strong { font-size: 15px; }
  .box-front .spf-seal { top: 695px; left: 74px; }
  .tube .spf-seal { top: 724px; left: 107px; }

  .volume { position: absolute; left: 0; right: 0; font-family: "Tinos", serif; font-weight: 700; font-size: 15px; }
  .box-side .volume, .box-front .volume { bottom: 70px; }
  .tube .volume { top: 804px; }

  .gold-band { position: absolute; left: 0; right: 0; height: 12px; border-top: 3px solid var(--gold); border-bottom: 2px solid var(--gold-light); }
  .box-side .gold-band, .box-front .gold-band { bottom: 40px; }
  .tube .gold-band { top: 836px; }

  .vine {
    position: absolute; left: 20px; top: 495px; width: 120px; height: 50px;
    background: linear-gradient(90deg, var(--green), var(--leaf)); border-radius: 25px; opacity: 0.85;
  }
  .web { position: absolute; left: 0; right: 0; top: 560px; font-size: 11px; color: var(--muted); }
  .caption-7 {
    position: absolute; left: 28px; top: 590px; width: 220px; height: 150px; text-align: left;
    font-family: "Tinos", serif; font-weight: 700; color: var(--deep-red);
  }
  .caption-7 .seven { position: absolute; left: 0; top: 0; font-size: 130px; line-height: 1; }
  .caption-7 .words { position: absolute; left: 70px; top: 58px; font-size: 20px; line-height: 1.1; width: 150px; }
  .caption-7 .one { font-size: 54px; line-height: 0.9; vertical-align: -8px; }

  .tube-cap {
    position: absolute; left: 760px; top: 940px; width: 280px; height: 80px;
    background: linear-gradient(90deg, var(--silver-dark), var(--silver) 35%, #f4f5f6 55%, var(--silver-dark));
  }
</style>
</head>
<body>
  <section class="panel box-side" aria-label="Box side panel">
    <div class="brand-mark"><span class="dot"></span><span class="brand-name">VelloBloom</span></div>
    <h2 class="product-title">ANTI-AGEING MOISTURISER</h2>
    <div class="flower" role="img" aria-label="Watercolour illustration of a pink tulip"></div>
    <div class="vine" role="img" aria-label="Green vine illustration curling around the numeral"></div>
    <p class="web">www.vellobloom-example.com.au</p>
    <p class="caption-7"><span class="seven">7</span><span class="words">Natural<br>Wonders in <span class="one">1</span></span></p>
    <p class="volume">75ml/2.5oz</p>
    <div class="gold-band"></div>
  </section>

  <section class="panel box-front" aria-label="Box front panel">
    <div class="brand-mark"><span class="dot"></span><span class="brand-name">VelloBloom</span></div>
    <h2 class="product-title">ANTI-AGEING MOISTURISER</h2>
    <div class="flower" role="img" aria-label="Watercolour illustration of a pink tulip"></div>
    <div class="portrait" role="img" aria-label="Photograph of a smiling woman with clear skin"></div>
    <div class="claims"><span class="organic">100% Organic</span><span class="paraben">Paraben Free</span></div>
    <div class="spf-seal"><strong>SPF 15</strong>NON-NANO<br>TECHNOLOGY</div>
    <p class="volume">75ml/2.5oz</p>
    <div class="gold-band"></div>
  </section>

  <section class="panel tube" aria-label="Tube front label">
    <div class="brand-mark"><span class="dot"></span><span class="brand-name">VelloBloom</span></div>
    <h2 class="product-title">ANTI-AGEING MOISTURISER</h2>
    <div class="flower" role="img" aria-label="Watercolour illustration of a pink tulip"></div>
    <div class="portrait" role="img" aria-label="Photograph of a smiling woman with clear skin"></div>
    <div class="claims"><span class="organic">100% Organic</span><span class="paraben">Paraben Free</span></div>
    <div class="spf-seal"><strong>SPF 15</strong>NON-NANO<br>TECHNOLOGY</div>
    <p class="volume">75ml/2.5oz</p>
    <div class="gold-band"></div>
  </section>
  <div class="tube-cap" aria-hidden="true"></div>
</body>
</html>
```